IT services company needs a business card designed

-2 sided business card.-Front is going to be the logo raised (3D floating effect) on a black background. Make the logos spider web shiny silver and keep the spider the same design. -Back needs to have the following information:Darrel Sotho, Managing Partner, Cell: 738-402-1954, Website: Plankhorn.com, Email: Darrel@Plankhorn.com
Target Market(s)
IT Services
Industry/Entity Type
It Company
Contact Information for Business Card
-2 sided business card.
-Front is going to be the logo raised (3D floating effect) on a black background. Make the logos spider web shiny silver and keep the spider the same design.
-Back needs to have the following information:
Darrel Sotho, Managing Partner, Cell: 738-402-1954, Website: Plankhorn.com, Email: Darrel@Plankhorn.com

```html
<!DOCTYPE html>
<html lang="en">
<head>
<meta charset="utf-8">
<title>Plankhorn Business Card</title>
<link href="https://fonts.googleapis.com/css2?family=Encode+Sans+Condensed:wght@400;500&family=Encode+Sans+Semi+Condensed:wght@400;500&display=swap" rel="stylesheet">
<style>
  :root {
    --stage: #808080;
    --card-black: #000000;
    --paper: #ffffff;
    --brand-blue: #14a3e6;
    --name-blue: #1a6fc6;
    --icon-grey: #c9c9c9;
    --emblem: #1b232b;
  }
  * { margin: 0; padding: 0; box-sizing: border-box; }
  html, body {
    width: 1066px; height: 1200px; overflow: hidden;
    background: var(--stage);
  }
  .canvas { position: relative; width: 1066px; height: 1200px; }

  .card { position: absolute; left: 36px; width: 988px; background: var(--card-black); overflow: hidden; }
  .card--front { top: 19px; height: 563px; }
  .card--back { top: 600px; height: 564px; }

  .emblem {
    position: absolute; left: 50%; top: 61px;
    width: 328px; height: 328px; margin-left: -164px;
    border-radius: 50%; background: var(--emblem);
  }
  .wordmark {
    position: absolute; left: 0; right: 0; top: 392px;
    text-align: center;
    font-family: "Encode Sans Semi Condensed", sans-serif;
    font-weight: 400; font-size: 82px; letter-spacing: 4px;
    color: var(--brand-blue); line-height: 1;
  }

  .name-panel { position: absolute; left: 0; top: 0; width: 532px; height: 564px; }
  .identity {
    position: absolute; left: 0; width: 460px; top: 226px;
    text-align: center; color: var(--name-blue);
  }
  .identity__name {
    font-family: "Encode Sans Semi Condensed", sans-serif;
    font-weight: 500; font-size: 50px; line-height: 1;
  }
  .identity__title {
    font-family: "Encode Sans Condensed", sans-serif;
    font-weight: 400; font-size: 31px; line-height: 1; margin-top: 8px;
  }

  .contacts { position: absolute; left: 624px; top: 194px; list-style: none; }
  .contact {
    display: flex; align-items: center; height: 62px;
    font-family: "Encode Sans Condensed", sans-serif;
    font-size: 32px; color: var(--brand-blue);
  }
  .contact svg { width: 34px; height: 34px; margin-right: 22px; flex: none; }
</style>
</head>
<body>
<main class="canvas">
  <section class="card card--front" aria-label="Card front">
    <div class="emblem"></div>
    <h1 class="wordmark">PLANKHORN</h1>
  </section>

  <section class="card card--back" aria-label="Card back">
    <svg class="name-panel" viewBox="0 0 532 564" aria-hidden="true">
      <path d="M0 0 H228 C420 0 532 140 532 280 C532 430 420 564 228 564 H0 Z" fill="var(--paper)"/>
    </svg>
    <div class="identity">
      <p class="identity__name">Darrel Sotho</p>
      <p class="identity__title">Managing Partner</p>
    </div>
    <ul class="contacts">
      <li class="contact">
        <svg viewBox="0 0 24 24" aria-hidden="true"><path fill="var(--icon-grey)" d="M7 2 L10 2 L11 7 L8.5 8.5 C9.5 12 11.5 14.5 15 16 L16.5 13.5 L21 15 L21 18 C20 21 17 22 13 20 C8 17 5 13 4.5 8 C4.3 5 5 3 7 2 Z"/></svg>
        <span>738-402-1954</span>
      </li>
      <li class="contact">
        <svg viewBox="0 0 24 24" aria-hidden="true"><rect x="2" y="5" width="20" height="14" fill="var(--icon-grey)"/><path d="M2 5 L12 13 L22 5" fill="none" stroke="#8a8a8a" stroke-width="1.2"/></svg>
        <span>Darrel@Plankhorn.com</span>
      </li>
      <li class="contact">
        <svg viewBox="0 0 24 24" aria-hidden="true" fill="none" stroke="var(--icon-grey)" stroke-width="1.4"><circle cx="12" cy="12" r="10"/><ellipse cx="12" cy="12" rx="4.5" ry="10"/><path d="M2 12 H22 M4 7 H20 M4 17 H20"/></svg>
        <span>Plankhorn.com</span>
      </li>
    </ul>
  </section>
</main>
</body>
</html>
```